Olive Oil Label Needs Graphic Designs

We need two sister label designs for 500ml bottles for our new brand "Casa Lumbre". Casa Lumbre is a high-end olive oil from Baeza, Spain which will be sold in the US. The oil will be produced from both Arbequina olives and Picual olives. Therefore, envisioning the same design just a different color scheme for the different labels.
The label should have the following characteristics; clean and simple, stand-out from mainstream labels, be eye-catching, give perception of high-end / high-quality.
Our current thinking of what we want (but please let your creative juices flow); lighter background, to be more eye catching, graphics of and olive, a olive branch or olive tree.
Text which should appear on the label are (not necessarily in this order);
Casa Lumbre
Extra Virgin Olive Oil
Family Reserve
Arbequina (One design)
Picual (Second design)
The label should be about 3 inches wide and 5.5 inches in height.

```html
<!DOCTYPE html>
<html lang="en">
<head>
<meta charset="utf-8">
<title>Casa Lumbre – Olive Oil Labels</title>
<link rel="stylesheet" href="https://fonts.googleapis.com/css2?family=Yellowtail&family=Open+Sans:wght@400&family=Libre+Baskerville&family=Kaushan+Script&display=swap">
<style>
  :root {
    --page: #ffffff;
    --label-dark: #262624;
    --label-mid: #3a3a37;
    --frame-light: #e6edc0;
    --frame-olive: #7f9a3a;
    --frame-deep: #4b6420;
    --ribbon: #2f4a2a;
    --ribbon-edge: #a9c06a;
    --ink: #ffffff;
    --ribbon-ink: #e9eedc;
    --leaf-light: #b9d84a;
    --leaf-deep: #3f6a1e;
    --glass-light: #8fa51c;
    --glass-deep: #354508;
    --cap: #1f3a22;
  }
  * { box-sizing: border-box; margin: 0; padding: 0; }
  html, body { width: 1200px; height: 900px; overflow: hidden; background: var(--page); }
  .canvas { position: relative; width: 1200px; height: 900px; }

  .label { position: absolute; width: 340px; height: 636px; overflow: hidden; }
  .label__shape { position: absolute; inset: 0; width: 100%; height: 100%; }
  .label__tree {
    position: absolute; left: 92px; top: 42px; width: 150px; height: 210px;
    background: radial-gradient(ellipse at 50% 30%, var(--leaf-light) 0%, #7aa52c 40%, var(--leaf-deep) 75%, transparent 76%);
    border-radius: 50% 50% 40% 40%;
  }
  .label__brand {
    position: absolute; left: 60px; right: 60px; top: 272px; text-align: center;
    white-space: nowrap;
    font-family: "Yellowtail", cursive; font-size: 44px; color: var(--ink); line-height: 1.1;
  }
  .label__product {
    position: absolute; left: 0; right: 0; top: 358px; text-align: center;
    white-space: nowrap;
    font-family: "Open Sans", sans-serif; font-size: 22px; color: var(--ink);
  }
  .label__ribbon { position: absolute; left: 46px; top: 402px; width: 258px; height: 56px; }
  .label__ribbon-text {
    position: absolute; left: 46px; top: 402px; width: 258px; height: 56px;
    display: flex; align-items: center; justify-content: center; white-space: nowrap;
    font-family: "Libre Baskerville", serif; font-size: 16px; color: var(--ribbon-ink); letter-spacing: 0.5px;
  }
  .label__variety {
    position: absolute; left: 0; right: 0; top: 518px; text-align: center; white-space: nowrap;
    font-family: "Kaushan Script", cursive; font-size: 30px; color: var(--ink); letter-spacing: 1px;
  }

  .label--arbequina { left: 21px; top: 142px; }
  .label--picual { left: 818px; top: 136px; }

  .bottle { position: absolute; top: 100px; width: 200px; height: 800px; }
  .bottle--arbequina { left: 395px; }
  .bottle--picual { left: 590px; }
  .bottle__body { position: absolute; inset: 0; width: 100%; height: 100%; }
  .bottle .label { left: 12px; top: 278px; transform: scale(0.5); transform-origin: 0 0; }
  .bottle--picual .label { left: 14px; }
</style>
</head>
<body>
<main class="canvas">

  <svg width="0" height="0" style="position:absolute">
    <defs>
      <linearGradient id="frameGrad" x1="0" y1="0" x2="1" y2="1">
        <stop offset="0" stop-color="#e6edc0"/>
        <stop offset="0.35" stop-color="#7f9a3a"/>
        <stop offset="0.6" stop-color="#dfe8b0"/>
        <stop offset="1" stop-color="#4b6420"/>
      </linearGradient>
      <linearGradient id="panelGrad" x1="0" y1="0" x2="1" y2="1">
        <stop offset="0" stop-color="#30302d"/>
        <stop offset="0.5" stop-color="#262624"/>
        <stop offset="1" stop-color="#33332f"/>
      </linearGradient>
      <linearGradient id="ribbonGrad" x1="0" y1="0" x2="0" y2="1">
        <stop offset="0" stop-color="#3d5e33"/>
        <stop offset="1" stop-color="#23391f"/>
      </linearGradient>
      <linearGradient id="glassGrad" x1="0" y1="0" x2="1" y2="0">
        <stop offset="0" stop-color="#354508"/>
        <stop offset="0.3" stop-color="#8fa51c"/>
        <stop offset="0.55" stop-color="#6c8010"/>
        <stop offset="1" stop-color="#2e3c06"/>
      </linearGradient>
    </defs>
  </svg>

  <section class="label label--arbequina">
    <svg class="label__shape" viewBox="0 0 340 636" preserveAspectRatio="none" aria-hidden="true">
      <path d="M0 0 H340 L308 318 L340 636 H0 L40 318 Z" fill="url(#frameGrad)"/>
      <path d="M10 10 H330 L298 318 L330 626 H10 L50 318 Z" fill="url(#panelGrad)"/>
    </svg>
    <div class="label__tree" role="img" aria-label="Stylised olive tree illustration"></div>
    <div class="label__brand">Casa Lumbre</div>
    <div class="label__product">Extra Virgin Olive Oil</div>
    <svg class="label__ribbon" viewBox="0 0 258 56" aria-hidden="true">
      <path d="M2 8 Q129 -2 256 8 L244 30 L256 52 Q129 42 2 52 L14 30 Z" fill="url(#ribbonGrad)" stroke="#a9c06a" stroke-width="2"/>
    </svg>
    <div class="label__ribbon-text">FAMILY RESERVE</div>
    <div class="label__variety">Arbequina</div>
  </section>

  <figure class="bottle bottle--arbequina">
    <svg class="bottle__body" viewBox="0 0 200 800" role="img" aria-label="Green glass olive oil bottle">
      <path d="M52 75 H148 V150 Q150 205 186 235 Q196 245 196 270 V800 H4 V270 Q4 245 14 235 Q50 205 52 150 Z" fill="url(#glassGrad)"/>
      <rect x="55" y="0" width="90" height="78" rx="4" fill="#1f3a22"/>
    </svg>
    <section class="label">
      <svg class="label__shape" viewBox="0 0 340 636" preserveAspectRatio="none" aria-hidden="true">
        <path d="M0 0 H340 L308 318 L340 636 H0 L40 318 Z" fill="url(#frameGrad)"/>
        <path d="M10 10 H330 L298 318 L330 626 H10 L50 318 Z" fill="url(#panelGrad)"/>
      </svg>
      <div class="label__tree" role="img" aria-label="Stylised olive tree illustration"></div>
      <div class="label__brand">Casa Lumbre</div>
      <div class="label__product">Extra Virgin Olive Oil</div>
      <svg class="label__ribbon" viewBox="0 0 258 56" aria-hidden="true">
        <path d="M2 8 Q129 -2 256 8 L244 30 L256 52 Q129 42 2 52 L14 30 Z" fill="url(#ribbonGrad)" stroke="#a9c06a" stroke-width="2"/>
      </svg>
      <div class="label__ribbon-text">FAMILY RESERVE</div>
      <div class="label__variety">Arbequina</div>
    </section>
  </figure>

  <figure class="bottle bottle--picual">
    <svg class="bottle__body" viewBox="0 0 200 800" role="img" aria-label="Green glass olive oil bottle">
      <path d="M52 75 H148 V150 Q150 205 186 235 Q196 245 196 270 V800 H4 V270 Q4 245 14 235 Q50 205 52 150 Z" fill="url(#glassGrad)"/>
      <rect x="55" y="0" width="90" height="78" rx="4" fill="#1f3a22"/>
    </svg>
    <section class="label">
      <svg class="label__shape" viewBox="0 0 340 636" preserveAspectRatio="none" aria-hidden="true">
        <path d="M0 0 H340 L308 318 L340 636 H0 L40 318 Z" fill="url(#frameGrad)"/>
        <path d="M10 10 H330 L298 318 L330 626 H10 L50 318 Z" fill="url(#panelGrad)"/>
      </svg>
      <div class="label__tree" role="img" aria-label="Stylised olive tree illustration"></div>
      <div class="label__brand">Casa Lumbre</div>
      <div class="label__product">Extra Virgin Olive Oil</div>
      <svg class="label__ribbon" viewBox="0 0 258 56" aria-hidden="true">
        <path d="M2 8 Q129 -2 256 8 L244 30 L256 52 Q129 42 2 52 L14 30 Z" fill="url(#ribbonGrad)" stroke="#a9c06a" stroke-width="2"/>
      </svg>
      <div class="label__ribbon-text">FAMILY RESERVE</div>
      <div class="label__variety">Picual</div>
    </section>
  </figure>

  <section class="label label--picual">
    <svg class="label__shape" viewBox="0 0 340 636" preserveAspectRatio="none" aria-hidden="true">
      <path d="M0 0 H340 L308 318 L340 636 H0 L40 318 Z" fill="url(#frameGrad)"/>
      <path d="M10 10 H330 L298 318 L330 626 H10 L50 318 Z" fill="url(#panelGrad)"/>
    </svg>
    <div class="label__tree" role="img" aria-label="Stylised olive tree illustration"></div>
    <div class="label__brand">Casa Lumbre</div>
    <div class="label__product">Extra Virgin Olive Oil</div>
    <svg class="label__ribbon" viewBox="0 0 258 56" aria-hidden="true">
      <path d="M2 8 Q129 -2 256 8 L244 30 L256 52 Q129 42 2 52 L14 30 Z" fill="url(#ribbonGrad)" stroke="#a9c06a" stroke-width="2"/>
    </svg>
    <div class="label__ribbon-text">FAMILY RESERVE</div>
    <div class="label__variety">Picual</div>
  </section>

</main>
</body>
</html>
```